Kestrel Summit 2019 Enemies of the End-Times Church Flyer

We want a church conference flyer designed. We are looking for a professional, yet catchy design that uses our brand colors and logo creatively while communicating key information of the event effectively. <br/>The flyer must include all of the following:<br/>Title: Kestrel Summit 2019<br/>Topic: The Enemies of The End-Times Church <br/>Subtitles: <br/> -How the antichrist raises an army by social behavior engineering. <br/>-How the architects of modern social constructs escaped the church's radar. <br/>-The Holy Spirit's end-times agenda:<br/> The Knock-Out Punch!<br/>Speaker: Prophet Marcus Toliver <br/>Dates/time: December 27, 28 & 29 at 6pm<br/>Location: Halvorn Community Center <br/> 241 Pellham Street <br/> Portland, ME 04102<br/>Contact info: phone: 207-555-0148 <br/>email: contact@brookmeadow.example <br/> www.vutel.example<br/>*The flyer must also include a picture of the speaker and our Vutel logo <br/>Thanks, we look forward to seeing what you come up with!

Colors

Designer to choose colors to be used in the design.

Requirements
Must have
• The flyer must include all of the following:
• Title: Kestrel Summit 2019
• Topic: The Enemies of The End-Times Church
• Subtitles:
• -How the antichrist raises an army by social behavior engineering.
• -How the architects of modern social constructs escaped the church's radar.
• -The Holy Spirit's end-times agenda:
• The Knock-Out Punch!
• Speaker: Prophet Marcus Toliver
• Dates/time: December 27, 28 & 29 at 6pm
• Location: Halvorn Community Center
• 241 Pellham Street
• Portland, ME 04102
• Contact info: phone: 207-555-0148
• email: contact@brookmeadow.example
• www.vutel.example
• *The flyer must also include a picture of the speaker and our Vutel logo
Should not have
• Pictures of crosses or church buildings

```html
<!DOCTYPE html>
<html lang="en">
<head>
<meta charset="utf-8">
<title>Kestrel Summit 2019 – The Enemies of the End-Times Church</title>
<link rel="stylesheet" href="https://fonts.googleapis.com/css2?family=Open+Sans:wght@400;600;700;800&display=swap">
<style>
  :root {
    --navy: #0c3560;
    --orange: #f08a12;
    --orange-bright: #f7a21b;
    --red: #e23a1c;
    --sky-blue: #3f8fd8;
    --peach: #f8c88d;
    --paper: #ffffff;
    --ink: #1b1b1b;
  }
  * { margin: 0; padding: 0; box-sizing: border-box; }
  html, body { width: 864px; height: 1200px; overflow: hidden; background: #ffffff; }
  body { font-family: "Open Sans", Arial, sans-serif; color: var(--ink); }

  .flyer { position: relative; width: 864px; height: 1200px; overflow: hidden;
    background: linear-gradient(100deg, var(--peach) 0%, #fde6c8 38%, #fbf4ec 62%, var(--paper) 100%); }

  .flyer__shapes { position: absolute; inset: 0; }

  .brand { position: absolute; top: 38px; right: 60px; display: flex; align-items: center; gap: 10px;
    color: #ffffff; font-weight: 600; font-size: 40px; letter-spacing: 1px; }
  .brand__dot { width: 16px; height: 16px; border-radius: 50%; background: var(--orange); }

  .title { position: absolute; left: 0; width: 864px; text-align: center; }
  .title__name { top: 160px; font-size: 58px; font-weight: 700; color: var(--sky-blue); line-height: 1; }
  .title__year { top: 222px; font-size: 60px; font-weight: 800; color: var(--orange-bright); line-height: 1; }
  .title__rule { position: absolute; top: 259px; height: 3px; background: var(--orange-bright); }
  .title__rule--left { left: 124px; width: 224px; }
  .title__rule--right { left: 542px; width: 213px; }
  .topic { position: absolute; top: 292px; left: 0; width: 864px; text-align: center;
    color: #ffffff; font-size: 27px; font-weight: 600; letter-spacing: 0.3px; }

  .talks { position: absolute; left: 58px; top: 550px; width: 322px; list-style: none; }
  .talks__item { position: relative; padding-left: 36px; font-size: 19px; line-height: 28px; margin-bottom: 18px; color: #222; }
  .talks__icon { position: absolute; left: 0; top: 4px; width: 20px; height: 28px; }

  .speaker { position: absolute; left: 427px; top: 756px; font-size: 21px; color: #1a1a1a; }
  .speaker__label { font-weight: 700; color: var(--navy); }

  .venue__pin { position: absolute; left: 398px; top: 844px; width: 40px; height: 56px; }
  .venue__name { position: absolute; top: 900px; left: 0; width: 864px; text-align: center;
    font-size: 44px; font-weight: 700; color: var(--orange); text-shadow: 1px 2px 2px rgba(0,0,0,.35); }
  .venue__address { position: absolute; top: 962px; left: 0; width: 864px; text-align: center;
    font-size: 26px; color: var(--navy); }

  .schedule { position: absolute; top: 1017px; left: 94px; height: 44px; display: flex; }
  .schedule__dates { width: 499px; background: var(--navy); color: #fff; font-weight: 700; font-size: 23px;
    display: flex; align-items: center; padding-left: 18px; }
  .schedule__time { width: 177px; background: var(--orange); color: var(--navy); font-weight: 700; font-size: 27px;
    display: flex; align-items: center; justify-content: center; }

  .contact { position: absolute; display: flex; align-items: center; gap: 7px; color: #fff; white-space: nowrap; }
  .contact--email { left: 0; top: 1127px; width: 256px; height: 73px; justify-content: center; font-size: 13px; font-weight: 600; }
  .contact--web { left: 613px; top: 1127px; width: 251px; height: 73px; justify-content: center; font-size: 13px; font-weight: 600; }
  .contact--phone { left: 260px; top: 1098px; width: 347px; height: 102px; justify-content: center;
    color: var(--ink); font-size: 36px; font-weight: 700; gap: 12px; }
  .contact__icon { width: 20px; height: 20px; flex: none; }
  .contact--phone .contact__icon { width: 34px; height: 34px; }
</style>
</head>
<body>
<main class="flyer">
  <svg class="flyer__shapes" width="864" height="1200" viewBox="0 0 864 1200">
    <defs>
      <linearGradient id="sunset" x1="0" y1="0" x2="0" y2="1">
        <stop offset="0" stop-color="#e8641a"/>
        <stop offset="0.2" stop-color="#f39a22"/>
        <stop offset="0.4" stop-color="#c9471a"/>
        <stop offset="0.62" stop-color="#3a1a12"/>
        <stop offset="1" stop-color="#0b0b10"/>
      </linearGradient>
      <radialGradient id="portrait" cx="0.5" cy="0.45" r="0.6">
        <stop offset="0" stop-color="#c9a36a"/>
        <stop offset="0.6" stop-color="#8b6a45"/>
        <stop offset="1" stop-color="#b8c4d6"/>
      </radialGradient>
    </defs>

    <path role="img" aria-label="Photo of a person with raised arms against a sunset sky"
          fill="url(#sunset)"
          d="M0 0 H864 V560 C760 520 640 500 520 470 C360 420 180 370 0 290 Z"/>

    <path fill="var(--orange)" d="M0 300 C180 380 360 430 520 478 C640 512 760 532 864 572 V582 C760 548 640 530 520 500 C340 455 170 405 0 322 Z"/>
    <path fill="var(--navy)" d="M0 322 C170 405 340 455 520 500 C640 530 760 548 864 582 V596 C760 566 640 548 520 520 C330 474 160 425 0 345 Z"/>

    <path fill="var(--navy)" d="M594 0 H864 V118 H656 C628 118 620 96 612 70 C604 40 600 16 594 0 Z"/>
    <rect x="849" y="110" width="15" height="400" fill="var(--navy)"/>

    <path fill="none" stroke="var(--navy)" stroke-width="22" d="M480 640 A185 185 0 0 1 700 380"/>
    <circle cx="621" cy="549" r="184" fill="none" stroke="var(--orange)" stroke-width="12"/>
    <path fill="none" stroke="var(--red)" stroke-width="16" d="M472 628 A185 185 0 0 0 800 600"/>
    <circle role="img" aria-label="Portrait photo of speaker Prophet Marcus Toliver" cx="621" cy="549" r="174" fill="url(#portrait)"/>

    <rect x="0" y="1127" width="256" height="73" fill="var(--navy)"/>
    <rect x="613" y="1127" width="251" height="73" fill="var(--navy)"/>
    <rect x="260" y="1098" width="347" height="102" fill="var(--orange)"/>
  </svg>

  <div class="brand"><span class="brand__dot"></span>VUTEL</div>

  <h1 class="title title__name">Kestrel Summit</h1>
  <span class="title__rule title__rule--left"></span>
  <span class="title__rule title__rule--right"></span>
  <p class="title title__year">2019</p>
  <h2 class="topic">THE ENEMIES OF THE END-TIMES CHURCH</h2>

  <ul class="talks">
    <li class="talks__item"><svg class="talks__icon" viewBox="0 0 20 28"><path fill="var(--navy)" d="M10 0 C14 8 20 12 20 19 A10 9 0 0 1 0 19 C0 13 5 10 6 4 C8 8 9 10 10 12 Z"/></svg>How the antichrist raises an army by social behavior engineering.</li>
    <li class="talks__item"><svg class="talks__icon" viewBox="0 0 20 28"><path fill="var(--navy)" d="M10 0 C14 8 20 12 20 19 A10 9 0 0 1 0 19 C0 13 5 10 6 4 C8 8 9 10 10 12 Z"/></svg>How the architects of modern social constructs escaped the church's radar.</li>
    <li class="talks__item"><svg class="talks__icon" viewBox="0 0 20 28"><path fill="var(--navy)" d="M10 0 C14 8 20 12 20 19 A10 9 0 0 1 0 19 C0 13 5 10 6 4 C8 8 9 10 10 12 Z"/></svg>The Holy Spirit's end-times agenda.</li>
    <li class="talks__item"><svg class="talks__icon" viewBox="0 0 20 28"><path fill="var(--navy)" d="M10 0 C14 8 20 12 20 19 A10 9 0 0 1 0 19 C0 13 5 10 6 4 C8 8 9 10 10 12 Z"/></svg>The Knock-Out Punch!</li>
  </ul>

  <p class="speaker"><span class="speaker__label">Speaker:</span> Prophet Marcus Toliver</p>

  <svg class="venue__pin" viewBox="0 0 40 56">
    <ellipse cx="20" cy="48" rx="17" ry="6" fill="none" stroke="#111" stroke-width="3"/>
    <path fill="var(--red)" d="M20 2 A14 14 0 0 1 34 16 C34 28 20 44 20 44 C20 44 6 28 6 16 A14 14 0 0 1 20 2 Z"/>
    <circle cx="20" cy="16" r="5" fill="#fff"/>
  </svg>
  <h3 class="venue__name">Halvorn Community Center</h3>
  <p class="venue__address">241 Pellham Street, Portland, ME 04102</p>

  <div class="schedule">
    <div class="schedule__dates">DECEMBER 27th 28th AND 29th,2019</div>
    <div class="schedule__time">TIME: 6pm</div>
  </div>

  <p class="contact contact--email">
    <svg class="contact__icon" viewBox="0 0 22 22"><circle cx="11" cy="11" r="10" fill="#fff"/><rect x="5" y="7" width="12" height="8" rx="1" fill="var(--navy)"/><path d="M5 7 L11 12 L17 7" fill="none" stroke="#fff" stroke-width="1.2"/></svg>
    contact@brookmeadow.example
  </p>
  <p class="contact contact--phone">
    <svg class="contact__icon" viewBox="0 0 34 34"><circle cx="17" cy="17" r="16" fill="var(--navy)"/><path fill="var(--orange)" d="M11 8 L14 8 L16 13 L14 15 C15 18 17 20 19 21 L21 19 L26 21 L26 24 C26 25 25 26 24 26 C16 26 8 18 8 10 C8 9 9 8 11 8 Z"/></svg>
    207-555-0148
  </p>
  <p class="contact contact--web">
    <svg class="contact__icon" viewBox="0 0 22 22"><g fill="none" stroke="#fff" stroke-width="1.5"><circle cx="11" cy="11" r="9.5"/><ellipse cx="11" cy="11" rx="4" ry="9.5"/><path d="M1.5 11 H20.5 M3 6 H19 M3 16 H19"/></g></svg>
    www.vutel.example
  </p>
</main>
</body>
</html>
```